Car Soap Label Design specifically targeting RVs

I am private labeling a car wash soap to specifically target the RV industry. It will be sold in a one gallon jug with a 6"x11" spot to place the label on front and wrap around the two sides. (see attached pics for example of label size) The front of the label I want to have a realistic picture of a high dollar class A RV somehow integrated into the design, and the key features of the soap. I had wordsmithbot design a couple that I kind of like the look of that I will attach, but open to other options. I want something clean and professional looking that will back the premium product I am selling.
The name of my brand is "Blue Harbor Gleam". I want the brand name to be somewhere on the label, but not a main focus. I want the focus to be the product and its benefits. "Premium RV Wash and Wax" as the main verbiage. Benefits... "Developed for Use With Foam Gun or Bucket with Water", "Safe for All RV Exteriors", "Protective Wax Formula", "Enhanced Shine", "Water Repellent", "Streak Free Rinse", "UV Protection". On the side...Directions: 2 Ways of Mixing... Pour Concentrate into Foam Gun Bottle OR Mixing Ratio: 1 Part Wash & Wax / 3 Parts Water in bucket. Apply soap to one side of RV at a time and use carwash brush to easily loosen road film and rinse clean. On the other side... Keep from freezing, Keep Out of Reach of Children. MADE IN USA. Hazardous Ingredients: NONE . NOTICE: The seller and/or manufacturer assumes no responsibility for damage or injury resulting from misuse of this product. No warranties, expressed or implied, are given for the performance or safety of this product.

Target Market(s)

RV industry

Industry/Entity Type

RV/Auto

Requirements
Must have
• Clean, Professional look, size 6" tall and 11" wide
Nice to have
• Realistic Class A RV as part of design

```html
<!DOCTYPE html>
<html lang="en">
<head>
<meta charset="utf-8">
<title>Premium RV Wash &amp; Wax Label</title>
<link rel="stylesheet" href="https://fonts.googleapis.com/css2?family=Montserrat:wght@400;500;600;700;800&family=Oswald:wght@500;600&display=swap">
<style>
  :root {
    --navy: #1f3c7a;
    --navy-deep: #17306a;
    --ink: #1b1b1b;
    --paper: #ffffff;
    --stage: #e9e9e9;
    --rule: #c9cfdc;
  }
  * { box-sizing: border-box; margin: 0; padding: 0; }
  html, body { width: 885px; height: 1200px; overflow: hidden; }
  body {
    background: var(--stage);
    font-family: "Montserrat", Arial, sans-serif;
    color: var(--ink);
    position: relative;
  }
  .label {
    position: absolute;
    left: 0; top: 358px;
    width: 885px; height: 483px;
    background: var(--paper);
    border: 1px solid var(--rule);
  }
  /* front panel */
  .front {
    position: absolute;
    left: 14px; top: 14px;
    width: 368px; height: 398px;
    background: var(--navy);
    color: var(--paper);
  }
  .front-title {
    position: absolute; left: 0; right: 0; top: 20px;
    text-align: center;
    font-family: "Oswald", "Arial Narrow", sans-serif;
    line-height: 1;
  }
  .front-title .kicker { font-size: 24px; font-weight: 500; letter-spacing: 1px; }
  .front-title .main { font-size: 52px; font-weight: 600; letter-spacing: 1px; margin-top: 4px; }
  .rv-art {
    position: absolute; left: 34px; top: 120px;
    width: 300px; height: 150px;
    background: linear-gradient(180deg, #f4f6fb 0%, #d6dcea 100%);
    border-radius: 18px 40px 6px 6px;
  }
  .for-all {
    position: absolute; right: 14px; top: 280px;
    font-size: 9px; font-weight: 700;
    background: var(--paper); color: var(--navy);
    padding: 2px 5px;
  }
  .front-name {
    position: absolute; left: 18px; right: 18px; top: 300px;
    text-align: center; line-height: 1;
  }
  .front-name .small { font-size: 15px; font-weight: 600; letter-spacing: 1px; text-align: left; }
  .front-name .big {
    font-family: "Oswald", "Arial Narrow", sans-serif;
    font-size: 52px; font-weight: 600; letter-spacing: 1px; margin-top: 2px;
  }
  .front-name .tag { font-size: 19px; font-weight: 700; margin-top: 4px; }
  .front-foot {
    position: absolute; left: 14px; top: 416px; width: 368px;
    display: flex; align-items: center; gap: 10px;
    font-size: 12px; color: var(--navy);
  }
  .front-foot .finish { font-weight: 800; letter-spacing: .5px; }
  .front-foot .bar { width: 1px; height: 14px; background: var(--navy); }
  .front-foot .brand { font-weight: 500; }

  /* spine */
  .spine {
    position: absolute; left: 396px; top: 14px;
    width: 70px; height: 455px;
  }
  .spine-text {
    position: absolute; left: 50%; top: 50%;
    width: 455px;
    transform: translate(-50%, -50%) rotate(90deg);
    text-align: center; color: var(--navy); line-height: 1.1;
  }
  .spine-text .line1 { font-size: 27px; font-weight: 800; }
  .spine-text .line2 { font-size: 18px; font-weight: 800; letter-spacing: 1px; }

  /* info panel */
  .info {
    position: absolute; left: 480px; top: 16px; width: 390px;
    font-size: 11px; line-height: 1.35;
  }
  .info h3 { font-size: 13px; font-weight: 700; text-decoration: underline; margin-bottom: 3px; }
  .benefits { list-style: none; padding-left: 12px; }
  .benefits li::before { content: "\2022"; margin-right: 6px; }
  .directions { margin-top: 26px; }
  .directions h3 { text-align: center; }
  .directions p { margin-bottom: 4px; }
  .directions .or { font-weight: 700; padding-left: 12px; }
  .warnings { margin-top: 10px; text-align: center; font-weight: 700; font-size: 12px; }
  .warnings .haz { font-weight: 500; }
  .notice { margin-top: 14px; font-size: 10px; }
  .notice h3 { font-size: 12px; }
  .made { position: absolute; right: 18px; bottom: 10px; font-size: 9px; font-weight: 600; }
</style>
</head>
<body>
<main class="label">
  <section class="front">
    <div class="front-title">
      <div class="kicker">PREMIUM RV</div>
      <div class="main">WASH &amp;WAX</div>
    </div>
    <div class="rv-art" role="img" aria-label="Illustration of a Class A motorhome, side view"></div>
    <span class="for-all">FOR ALL RV</span>
    <div class="front-name">
      <div class="small">PREMIUM RV</div>
      <div class="big">WASH &amp; WAX</div>
      <div class="tag">CLEANS &amp;PROTECTS</div>
    </div>
  </section>
  <div class="front-foot">
    <span class="finish">FOR STREAK-FREE FINISH</span>
    <span class="bar"></span>
    <span class="brand">Blue Harbor Gleam</span>
  </div>

  <section class="spine">
    <div class="spine-text">
      <div class="line1">Premium RV Wash and Wax</div>
      <div class="line2">1 GALLON JUG</div>
    </div>
  </section>

  <section class="info">
    <h3>Benefits:</h3>
    <ul class="benefits">
      <li>Developed for Use With Foam Gun or Bucket with Water</li>
      <li>Safe for All RV Exteriors</li>
      <li>Protective Wax Formula</li>
      <li>Enhanced Shine</li>
      <li>Water Repellent</li>
      <li>Streak Free Rinse</li>
      <li>UV Protection</li>
    </ul>

    <div class="directions">
      <h3>Directions:</h3>
      <p>&bull; Pour Concentrate into Foam Gun Bottle</p>
      <p class="or">OR</p>
      <p>&bull; 1 Part Wash &amp; Wax / 3 Parts Water in bucket.<br>
        Apply soap to one side of RV at a time and use carwash brush to easily loosen road film and rinse clean.</p>
    </div>

    <div class="warnings">
      <p>&bull; Keep from freezing</p>
      <p>&bull; Keep Out of Reach of Children</p>
      <p class="haz">Hazardous Ingredients: <strong>NONE.</strong></p>
    </div>

    <div class="notice">
      <h3>NOTICE:</h3>
      <p>The seller and/or manufacturer assumes no responsibility for damage or injury resulting from misuse of this product. No warranties, expressed or implied, are given for the performance or safety of this product.</p>
    </div>
  </section>
  <span class="made">MADE IN USA</span>
</main>
</body>
</html>
```